Fernvale Business Card Design

We are looking for a fresh business card design for our new logo. We would like a business card that is unique but friendly. We are in the window coverings business offering blinds, shutters and shades for homes.

Target Market(s)

Targeting the end-consumer

Industry/Entity Type

Business

Requirements
Must have
• Must have a dedicates space for a photo of our sales person. Must contain our new logo (attached).

```html
<!DOCTYPE html>
<html lang="en">
<head>
<meta charset="utf-8">
<title>Fernvale Business Card</title>
<link href="https://fonts.googleapis.com/css2?family=Lato:wght@400;700&display=swap" rel="stylesheet">
<style>
  :root {
    --stage: #242424;
    --card-light: #f4f4f4;
    --leaf-green: #8dc63f;
    --ink: #4f4f4f;
    --rule: #8a8a8a;
    --white: #ffffff;
    --photo-top: #dfe6d6;
    --photo-bottom: #c4cfb6;
  }
  * { margin: 0; padding: 0; box-sizing: border-box; }
  html, body {
    width: 1200px;
    height: 900px;
    overflow: hidden;
    background: var(--stage);
    font-family: "Lato", Arial, sans-serif;
  }
  .stage { position: relative; width: 1200px; height: 900px; }
  .card {
    position: absolute;
    top: 306px;
    width: 440px;
    height: 271px;
    border-radius: 10px;
    overflow: hidden;
    box-shadow: 0 3px 8px rgba(0,0,0,0.55);
  }
  .card-front { left: 149px; background: var(--card-light); color: var(--ink); }
  .card-back { left: 608px; background: var(--leaf-green); }

  .sales-photo {
    position: absolute;
    left: 21px;
    top: 26px;
    width: 92px;
    height: 108px;
    border-radius: 4px;
    border: 2px solid var(--leaf-green);
    background: linear-gradient(180deg, var(--photo-top), var(--photo-bottom));
  }

  .brand {
    position: absolute;
    right: 24px;
    top: 56px;
    display: flex;
    align-items: center;
    gap: 12px;
  }
  .brand-square {
    width: 40px; height: 40px;
    background: var(--leaf-green);
    border-radius: 3px;
  }
  .brand-name {
    font-size: 38px;
    font-weight: 400;
    color: #5a5a5a;
    line-height: 1;
  }

  .person { position: absolute; left: 21px; top: 152px; right: 24px; }
  .person-row { display: flex; align-items: center; gap: 6px; height: 22px; }
  .person-name { font-size: 18px; font-weight: 700; color: var(--leaf-green); white-space: nowrap; line-height: 22px; }
  .person-rule { flex: 1; height: 1px; background: var(--rule); margin-top: 4px; }
  .person-title { font-size: 13px; line-height: 16px; margin-top: -2px; }

  .address {
    position: absolute; left: 21px; top: 217px;
    font-size: 13px; line-height: 16px;
  }
  .contacts {
    position: absolute; right: 24px; top: 186px;
    list-style: none; font-size: 13px; line-height: 16px;
  }
  .contacts li { display: flex; justify-content: flex-end; align-items: center; gap: 5px; }
  .contact-icon { width: 12px; height: 12px; display: block; }

  .back-fill { position: absolute; inset: 0; background: var(--leaf-green); }
  .back-brand {
    position: absolute; right: 64px; top: 155px;
    display: flex; align-items: center; gap: 10px;
  }
  .back-brand-square {
    width: 56px; height: 56px;
    border: 3px solid var(--white); border-radius: 4px;
  }
</style>
</head>
<body>
<div class="stage">

  <section class="card card-front">
    <div class="sales-photo" role="img" aria-label="Space for the salesperson's photo"></div>

    <div class="brand">
      <span class="brand-square"></span>
      <span class="brand-name">Fernvale</span>
    </div>

    <div class="person">
      <div class="person-row">
        <span class="person-name">Daniel Hartley</span>
        <span class="person-rule"></span>
      </div>
      <div class="person-title">Managing Director</div>
    </div>

    <ul class="contacts">
      <li>044-987 650 321
        <svg class="contact-icon" viewBox="0 0 12 12"><rect width="12" height="12" rx="2.5" fill="#8dc63f"/><path d="M3 5 Q6 2 9 5 L8 6 L7 5 L5 5 L4 6 Z M3.5 6.5 H8.5 V9 H3.5 Z" fill="#fff"/></svg></li>
      <li>044-987 650 321
        <svg class="contact-icon" viewBox="0 0 12 12"><rect width="12" height="12" rx="2.5" fill="#8dc63f"/><rect x="4" y="2.5" width="4" height="7" rx="0.8" fill="none" stroke="#fff" stroke-width="1"/></svg></li>
      <li>hello@fernvalehome.com
        <svg class="contact-icon" viewBox="0 0 12 12"><rect width="12" height="12" rx="2.5" fill="#8dc63f"/><rect x="2.5" y="3.5" width="7" height="5" fill="#fff"/><path d="M2.5 3.5 L6 6.3 L9.5 3.5" fill="none" stroke="#8dc63f" stroke-width="0.8"/></svg></li>
      <li>www.fernvalehome.com
        <svg class="contact-icon" viewBox="0 0 12 12"><rect width="12" height="12" rx="2.5" fill="#8dc63f"/><circle cx="6" cy="6" r="3.5" fill="#fff"/><path d="M2.5 6 H9.5 M6 2.5 V9.5" stroke="#8dc63f" stroke-width="0.7"/></svg></li>
    </ul>

    <div class="address">
      <p>12345, Address Goes Here</p>
      <p>Country Name, 123456.</p>
    </div>
  </section>

  <section class="card card-back">
    <div class="back-fill" role="img" aria-label="Green background with a faint repeating leaf pattern"></div>
    <div class="back-brand">
      <span class="back-brand-square"></span>
    </div>
  </section>

</div>
</body>
</html>
```